Roadside building business signage for a holistic health clinic.

Replace signs as shown in the attached file. They are perforated stickers that go on the windows as shown. Looking for something that has our logo and says the name of the practice with logo (Fernbrook Health & Wellness) also boldly says Acupuncture, IV Vitamins, and Holistic Health.
Possibly our phone number as well 318-627-5194
Updates

Please don't use pink except the logo. Earthy, organic tone colors appreciated.

Need of eye catching window signage of a holistic clinic on a brick building. Pink, purple, sage green, white color. Logo is pink on a white background. Please don't overload with too much pink. Words to include are "Fernbrook Health and Wellness(name of business)", "Direct Primary Care", " Medical acupuncture", "IV Vitamin Therapy", "fernbrookcare-example.com","318-627-5194".

Target Market(s)

People will see in their cars passing by the building. Busy roadside so need to be visible while passing in fast speed.

Industry/Entity Type

Health & Wellness

Font styles to use
Sans Serif

Colors

Designer to choose colors to be used in the design.

Requirements
Must have
• On sign must have words Holistic Medicine, Medical Acupuncture, Direct Primary Care and IV vitamins.
Nice to have
• Simple, minimalistic, artistic yet has clear message. White, Black, Violet, Pink (logo), Dark green, Sage green.
Should not have
• Bold colors (red, yellow, blue), same tone colors. Blue waves on the current signage (uploaded file) must go.

```html
<!DOCTYPE html>
<html lang="en">
<head>
<meta charset="utf-8">
<title>Fernbrook Health &amp; Wellness – Window Signage</title>
<link rel="stylesheet" href="https://fonts.googleapis.com/css2?family=Marcellus&display=swap">
<style>
  :root {
    --forest: #0f4d3a;
    --mist-top: #ffffff;
    --mist-bottom: #d9eee1;
    --blossom: #e2458f;
    --canvas: #ffffff;
  }
  html, body {
    margin: 0;
    padding: 0;
    width: 1200px;
    height: 613px;
    overflow: hidden;
    background: var(--canvas);
  }
  .signage {
    position: absolute;
    left: 254px;
    top: 46px;
    width: 691px;
    height: 521px;
  }
  .panel-face { fill: url(#mist); }
  .panel-frame {
    fill: none;
    stroke: var(--forest);
    stroke-width: 6;
    stroke-linejoin: miter;
  }
  .brand-mark { fill: var(--blossom); }
  .sign-text {
    font-family: "Marcellus", serif;
    fill: var(--forest);
    text-anchor: middle;
  }
  .brand-name { font-size: 56px; letter-spacing: 5px; }
  .brand-sub { font-size: 17px; letter-spacing: 6px; }
  .services { font-size: 25px; }
  .phone { font-size: 54px; font-weight: 700; }
  .website { font-size: 20px; letter-spacing: 1px; }
</style>
</head>
<body>
  <svg class="signage" viewBox="60 48 926 698" xmlns="http://www.w3.org/2000/svg">
    <defs>
      <linearGradient id="mist" x1="0" y1="0" x2="0" y2="1">
        <stop offset="0" stop-color="var(--mist-top)"/>
        <stop offset="1" stop-color="var(--mist-bottom)"/>
      </linearGradient>
    </defs>

    <g class="panel panel-left">
      <path class="panel-face" d="M64,740 L64,283 L293,283 C300,180 380,80 522,52 L522,740 Z"/>
      <path class="panel-frame" d="M64,740 L64,283 L293,283 C300,180 380,80 522,52 L522,740 Z"/>
      <circle class="brand-mark" cx="292" cy="372" r="34"/>
      <text class="sign-text brand-name" x="292" y="470">FERNBROOK</text>
      <text class="sign-text brand-sub" x="292" y="498">HEALTH &amp; WELLNESS</text>
      <text class="sign-text services" x="292" y="552">Direct Primary Care</text>
      <text class="sign-text services" x="292" y="584">Medical Acupuncture</text>
      <text class="sign-text services" x="292" y="616">IV Vitamins &amp; Holistic Medicine</text>
      <text class="sign-text phone" x="292" y="684">318-627-5194</text>
      <text class="sign-text website" x="292" y="722">fernbrookcare-example.com</text>
    </g>

    <g class="panel panel-right">
      <path class="panel-face" d="M522,52 C664,80 744,180 751,283 L981,283 L981,740 L522,740 Z"/>
      <path class="panel-frame" d="M522,52 C664,80 744,180 751,283 L981,283 L981,740 L522,740 Z"/>
      <circle class="brand-mark" cx="752" cy="372" r="34"/>
      <text class="sign-text brand-name" x="752" y="470">FERNBROOK</text>
      <text class="sign-text brand-sub" x="752" y="498">HEALTH &amp; WELLNESS</text>
      <text class="sign-text services" x="752" y="552">Direct Primary Care</text>
      <text class="sign-text services" x="752" y="584">Medical Acupuncture</text>
      <text class="sign-text services" x="752" y="616">IV Vitamins &amp; Holistic Medicine</text>
      <text class="sign-text phone" x="752" y="684">318-627-5194</text>
      <text class="sign-text website" x="752" y="722">fernbrookcare-example.com</text>
    </g>
  </svg>
</body>
</html>
```